Advertisements for web banners and street signage

Role Finch is a New Zealand Job Board (career vacancy search) website that requires some creative ad banners for promotion online, at events, and on street signage.

Our role finch logo is attached in low resolution, and in high resolution, the logo, slogan, and website should be incorporated somewhere in the ad. Ads should be long in length (not square) either vertical or horizontal.

I've attached some examples of ads

Target Market(s)

Working population. We exist to bring more choice to New Zealand job seekers and save job seekers time. We are about "finding your next job"

Industry/Entity Type

Recruitment

Requirements
Must have
• Use of bright colours. Gets your attention.
Nice to have
• A funny image or joke related to finding a job that catches your attention e.g. could play on the use of Role Finch = job "sauce"
• A slogan, pun, or sentence related to finding a job that catches your attention, An example of a slogans "some say a change is as good as a holiday"
Should not have
• Swearing or sexism

```html
<!DOCTYPE html>
<html lang="en">
<head>
<meta charset="utf-8">
<title>Role Finch – Get the Perfect One</title>
<link rel="stylesheet" href="https://fonts.googleapis.com/css2?family=Roboto+Condensed:wght@400;700&display=swap">
<style>
  :root {
    --backdrop: #e4e5e6;
    --poster: #ffffff;
    --ink: #1c1c1c;
    --accent-red: #e0141b;
    --teal: #12a08e;
    --muted: #4a4a4a;
    --logo-grey: #5e6166;
  }
  * { margin: 0; padding: 0; box-sizing: border-box; }
  html, body {
    width: 1200px;
    height: 905px;
    overflow: hidden;
    background: var(--backdrop);
  }
  .canvas {
    position: relative;
    width: 1200px;
    height: 905px;
  }
  .poster {
    position: absolute;
    left: 332px;
    top: 20px;
    width: 536px;
    height: 865px;
    background: var(--poster);
    font-family: "Roboto Condensed", "Arial Narrow", sans-serif;
  }
  .job-grid {
    position: absolute;
    left: 17px;
    right: 14px;
    top: 18px;
  }
  .job-row {
    font-weight: 700;
    font-size: 31px;
    line-height: 32.6px;
    color: var(--ink);
    text-align: justify;
    text-align-last: justify;
    letter-spacing: -0.5px;
    white-space: normal;
  }
  .job-row .highlight {
    font-style: normal;
    color: var(--accent-red);
  }
  .headline {
    position: absolute;
    left: 0;
    right: 0;
    top: 632px;
    text-align: center;
    font-weight: 700;
    font-size: 41px;
    color: var(--teal);
    letter-spacing: 0.2px;
  }
  .brand {
    position: absolute;
    left: 0;
    right: 0;
    top: 716px;
    display: flex;
    flex-direction: column;
    align-items: center;
  }
  .brand-dot {
    width: 44px;
    height: 44px;
    border-radius: 50%;
    border: 2px solid var(--logo-grey);
  }
  .brand-name {
    margin-top: 10px;
    font-weight: 400;
    font-size: 15px;
    letter-spacing: 2px;
    text-transform: uppercase;
    color: var(--teal);
  }
  .brand-tagline {
    margin-top: 2px;
    font-size: 7px;
    letter-spacing: 1.5px;
    text-transform: uppercase;
    color: var(--logo-grey);
  }
  .website {
    position: absolute;
    left: 0;
    right: 0;
    top: 809px;
    text-align: center;
    font-size: 18px;
    color: var(--muted);
  }
</style>
</head>
<body>
<div class="canvas">
  <section class="poster">
    <div class="job-grid">
      <p class="job-row">JOB JOB JOB JOB JOB JOB JOB JOB JOB</p>
      <p class="job-row">JOB JOB JOB JOB JOB JOB JOB JOB JOB</p>
      <p class="job-row">JOB JOB JOB JOB JOB JOB JOB JOB JOB</p>
      <p class="job-row">JOB JOB JOB JOB JOB JOB JOB JOB JOB</p>
      <p class="job-row">JOB JOB JOB JOB JOB JOB JOB JOB JOB</p>
      <p class="job-row">JOB JOB JOB JOB JOB JOB JOB JOB JOB</p>
      <p class="job-row">JOB JOB JOB JOB JOB JOB JOB JOB JOB</p>
      <p class="job-row">JOB JOB JOB JOB <em class="highlight">JOB</em> JOB JOB JOB JOB</p>
      <p class="job-row">JOB JOB JOB JOB JOB JOB JOB JOB JOB</p>
      <p class="job-row">JOB JOB JOB JOB JOB JOB JOB JOB JOB</p>
      <p class="job-row">JOB JOB JOB JOB JOB JOB JOB JOB JOB</p>
      <p class="job-row">JOB JOB JOB JOB JOB JOB JOB JOB JOB</p>
      <p class="job-row">JOB JOB JOB JOB JOB JOB JOB JOB JOB</p>
      <p class="job-row">JOB JOB JOB JOB JOB JOB JOB JOB JOB</p>
      <p class="job-row">JOB JOB JOB JOB JOB JOB JOB JOB JOB</p>
      <p class="job-row">JOB JOB JOB JOB JOB JOB JOB JOB JOB</p>
      <p class="job-row">JOB JOB JOB JOB JOB JOB JOB JOB JOB</p>
    </div>

    <h1 class="headline">GET THE PERFECT ONE</h1>

    <div class="brand">
      <span class="brand-dot"></span>
      <span class="brand-name">Role Finch</span>
      <span class="brand-tagline">find your next job</span>
    </div>

    <p class="website">www.rolefinch.co.nz</p>
  </section>
</div>
</body>
</html>
```